Letterhead for clinic notes, test reports, and business cards

I need business card and letterheads for a medical clinic with the following:
1- Business cards. The back should allow for space for date and time of next appointments (few lines would do)
2- Letterhead for clinic notes
3- Letterhead for test reports.

Feel free to use whats included for examples. I value creativity so be creative.

Target Market(s)

Patients, referring physicians.

Industry/Entity Type

Health Care

Requirements
Must have
• Must use current logo.
• Must look good on white background
• Letterhead and reports must look good faxed.
• Please use themes of the current logo. Another possible color to use is grey as well (www.brambleveincare.org - use the font color in the text of that website)

```html
<!DOCTYPE html>
<html lang="en">
<head>
<meta charset="utf-8">
<title>Bramblevein Care Institute – Business Card</title>
<link rel="stylesheet" href="https://fonts.googleapis.com/css2?family=Nunito+Sans:wght@400;600;700&display=swap">
<style>
  :root {
    --page-bg: #e9eaec;
    --card-white: #ffffff;
    --blue-deep: #1f2a78;
    --blue-mid: #1d56ad;
    --blue-bright: #2a74c9;
    --ink-blue: #1d4f8c;
    --ink-dark: #2a2a2a;
    --rule: #8a96aa;
    --white: #ffffff;
  }
  * { box-sizing: border-box; margin: 0; padding: 0; }
  html, body {
    width: 1105px; height: 1200px; overflow: hidden;
    background: var(--page-bg);
    font-family: "Nunito Sans", sans-serif;
  }
  .card {
    position: absolute; left: 193px; width: 720px; height: 410px;
    background: var(--card-white); overflow: hidden;
    box-shadow: 0 2px 6px rgba(0,0,0,.18);
  }
  .card--front { top: 167px; }
  .card--back { top: 623px; color: var(--ink-blue); }

  /* front */
  .front-panel { position: absolute; inset: 0; width: 100%; height: 100%; }
  .holder { position: absolute; left: 43px; top: 40px; color: var(--white); }
  .holder__name { font-size: 28px; font-weight: 700; line-height: 1.1; }
  .holder__role { font-size: 19px; font-weight: 400; margin-top: 2px; }
  .address {
    position: absolute; left: 43px; top: 176px; color: var(--white);
    font-size: 18px; line-height: 25px; font-style: normal;
  }
  .contacts { position: absolute; left: 43px; top: 262px; list-style: none; color: var(--white); font-size: 18px; }
  .contacts li { display: flex; align-items: center; height: 28px; }
  .contacts svg { width: 17px; height: 17px; margin-right: 13px; fill: var(--white); }
  .website { position: absolute; left: 43px; top: 350px; color: var(--white); font-size: 18px; }
  .front-brand {
    position: absolute; right: 36px; top: 170px; width: 250px;
    text-align: center; color: var(--ink-blue);
    font-size: 24px; font-weight: 700; letter-spacing: 1px; line-height: 1.25;
  }

  /* back */
  .brand {
    position: absolute; left: 430px; top: 48px; width: 250px; text-align: center;
    font-size: 22px; font-weight: 700; letter-spacing: 1px; line-height: 1.2; color: var(--ink-blue);
  }
  .appt__title { position: absolute; left: 41px; top: 100px; font-size: 28px; font-weight: 600; }
  .field { position: absolute; display: flex; align-items: baseline; font-size: 21px; }
  .field__line { border-bottom: 1.5px dotted var(--rule); height: 1px; margin-left: 12px; align-self: flex-end; margin-bottom: 6px; }
  .field--name { left: 44px; top: 164px; }
  .field--name .field__line { width: 545px; }
  .field--date { left: 44px; top: 226px; }
  .field--date .field__line { width: 265px; }
  .field--time { left: 393px; top: 226px; }
  .field--time .field__line { width: 140px; }
  .field__suffix { font-size: 15px; margin-left: 8px; }
  .days { position: absolute; left: 44px; right: 52px; top: 290px; display: flex; justify-content: space-between; list-style: none; font-size: 19px; }
  .days li { display: flex; align-items: center; }
  .days li::after { content: ""; width: 18px; height: 18px; border: 1.5px solid var(--ink-blue); margin-left: 8px; }
  .notice { position: absolute; left: 0; right: 0; top: 348px; text-align: center; font-size: 15px; color: var(--ink-dark); }
</style>
</head>
<body>

<section class="card card--front" aria-label="Business card front">
  <svg class="front-panel" viewBox="0 0 720 410" preserveAspectRatio="none" aria-hidden="true">
    <defs>
      <radialGradient id="panelGlow" cx="0.45" cy="0.4" r="0.75">
        <stop offset="0" stop-color="var(--blue-bright)"/>
        <stop offset="0.55" stop-color="var(--blue-mid)"/>
        <stop offset="1" stop-color="var(--blue-deep)"/>
      </radialGradient>
    </defs>
    <path d="M0 0 H350 C300 110 330 290 520 410 H0 Z" fill="url(#panelGlow)"/>
  </svg>

  <div class="holder">
    <h1 class="holder__name">Marcus Ellery</h1>
    <p class="holder__role">CEO/Founder</p>
  </div>

  <address class="address">1870 Larkspur Avenue<br>Suite 305<br>Ashford ON K4R2P8</address>

  <ul class="contacts">
    <li><svg viewBox="0 0 24 24"><path d="M6.6 10.8a15 15 0 0 0 6.6 6.6l2.2-2.2c.3-.3.7-.4 1-.2 1.1.4 2.3.6 3.6.6.6 0 1 .4 1 1V20c0 .6-.4 1-1 1A17 17 0 0 1 3 4c0-.6.4-1 1-1h3.5c.6 0 1 .4 1 1 0 1.3.2 2.5.6 3.6.1.3 0 .7-.2 1z"/></svg>555-310-4827</li>
    <li><svg viewBox="0 0 24 24"><path d="M6 2h9l3 3v4H6zM3 10h18v9h-3v3H6v-3H3zm5 6v4h8v-4z"/></svg>555-310-4830</li>
    <li><svg viewBox="0 0 24 24"><path d="M2 5h20v14H2zm2 2v.5l8 5 8-5V7z"/></svg>contact@brambleveincare.org</li>
  </ul>

  <p class="website">www.brambleveincare.org</p>

  <p class="front-brand">BRAMBLEVEIN CARE INSTITUTE</p>
</section>

<section class="card card--back" aria-label="Business card back">
  <p class="brand">BRAMBLEVEIN CARE<br>INSTITUTE</p>

  <h2 class="appt__title">Next Appointment</h2>

  <div class="field field--name"><span>Name :</span><span class="field__line"></span></div>
  <div class="field field--date"><span>Date :</span><span class="field__line"></span></div>
  <div class="field field--time"><span>Time :</span><span class="field__line"></span><span class="field__suffix">AM/PM</span></div>

  <ul class="days">
    <li>Sun</li><li>Mon</li><li>Tue</li><li>Wed</li><li>Thu</li><li>Fri</li><li>Sat</li>
  </ul>

  <p class="notice">If you are unable to keep your appointment please call the office 24 hours in advance.</p>
</section>

</body>
</html>
```